Security Cheat Sheets

We are after a nicely presented easy to follow cheat sheet around security such as Phishing and scams and acceptable use we can send to our clients for awareness.
The example Cheat Sheets is some info we would like (was something i downloaded from the internet so do not copy verbatim but has some good content ideas we would like to use) and a very simple example i prepared plus our logos etc.

```html
<!DOCTYPE html>
<html lang="en">
<head>
<meta charset="utf-8">
<title>Phishing and Scams – Cheat Sheet</title>
<link href="https://fonts.googleapis.com/css2?family=Oswald:wght@500;700&family=Roboto:wght@400;500;700;900&display=swap" rel="stylesheet">
<style>
:root{
  --navy:#1b2a5c;
  --blue:#1f4fb8;
  --blue-bright:#2c6be0;
  --red:#e02a2a;
  --green:#2faa4a;
  --grey-text:#5a6070;
  --sheet:#ffffff;
  --backdrop:#e9ebef;
  --rule:#c9cfdc;
}
*{margin:0;padding:0;box-sizing:border-box}
html,body{width:1200px;height:2400px;overflow:hidden}
body{background:var(--backdrop);font-family:'Roboto',Arial,sans-serif;position:relative}
.sheet{position:absolute;left:50px;top:350px;width:1100px;height:1700px;background:var(--sheet);overflow:hidden;box-shadow:0 4px 18px rgba(0,0,0,.12)}
.top-stripe{height:14px;background:linear-gradient(90deg,var(--blue),var(--blue-bright))}
.corner-band{position:absolute;right:0;top:14px;width:110px;height:250px;background:linear-gradient(180deg,var(--blue-bright),var(--blue));clip-path:polygon(40% 0,100% 0,100% 100%,0 100%)}
.corner-band-red{position:absolute;right:88px;top:14px;width:26px;height:250px;background:var(--red);clip-path:polygon(60% 0,100% 0,40% 100%,0 100%)}

.header{position:relative;height:250px;display:flex;align-items:center;padding:0 130px 0 44px;gap:30px}
.alert-badge{flex:none;width:160px;height:160px}
.title{font-family:'Oswald',Impact,sans-serif;font-weight:700;font-size:76px;line-height:1;color:var(--navy);letter-spacing:1px;white-space:nowrap}
.title .accent{color:var(--red)}
.subtitle{font-family:'Roboto',Arial,sans-serif;font-weight:900;font-size:33px;line-height:1.12;color:var(--navy);text-transform:uppercase;margin-top:10px}

.section-head{display:flex;align-items:center;gap:22px;padding:0 44px;height:110px}
.section-icon{flex:none;width:88px;height:88px}
.section-title{font-family:'Oswald',Impact,sans-serif;font-weight:700;font-size:48px;color:var(--navy);white-space:nowrap}
.section-rule{flex:1;height:4px;background:var(--rule)}

.checklist{padding:6px 70px 0 60px}
.checklist h3{font-family:'Roboto',Arial,sans-serif;font-weight:900;font-size:25px;color:var(--navy);text-transform:uppercase;margin:14px 0 12px}
.checklist ul{list-style:none}
.checklist li{display:flex;align-items:flex-start;gap:18px;font-size:21px;line-height:1.3;color:#2b2f3a;margin-bottom:14px}
.checklist li svg{flex:none;width:28px;height:28px;margin-top:0}

.bottom{display:flex;gap:36px;padding:40px 44px 0 44px}
.hacked{width:560px}
.hacked h2{font-family:'Oswald',Impact,sans-serif;font-weight:700;font-size:50px;line-height:1.02;color:var(--navy)}
.hacked h2 .accent{color:var(--red);display:block}
.hacked-cards{display:flex;gap:20px;margin-top:40px}
.info-card{position:relative;flex:1;background:linear-gradient(160deg,var(--blue-bright),var(--blue));border-radius:30px;padding:74px 22px 26px;color:#fff;font-size:19px;line-height:1.32;min-height:330px}
.info-card svg{position:absolute;left:22px;top:-26px;width:78px;height:78px}

.todo{flex:1;padding-top:4px}
.todo h2{font-family:'Oswald',Impact,sans-serif;font-weight:700;font-size:54px;line-height:1.02;color:var(--blue-bright)}
.todo p{margin-top:18px;font-size:23px;line-height:1.32;color:var(--grey-text)}
.brand{display:flex;align-items:center;gap:14px;margin-top:26px}
.brand-mark{width:44px;height:44px;background:var(--blue)}
.brand-name{font-family:'Roboto',Arial,sans-serif;font-weight:900;font-size:27px;color:var(--navy);letter-spacing:.5px}
.brand-tag{font-size:16px;color:var(--navy);margin:4px 0 0 58px}
.contacts{list-style:none;margin-top:20px}
.contacts li{display:flex;align-items:center;gap:16px;font-size:25px;font-weight:500;color:var(--navy);margin-bottom:14px}
.contacts svg{flex:none;width:34px;height:34px}

.footer{position:absolute;left:0;right:0;bottom:0;height:70px;background:linear-gradient(90deg,var(--blue),var(--blue-bright))}
.footer-red{position:absolute;right:0;bottom:70px;width:420px;height:14px;background:var(--red);clip-path:polygon(4% 0,100% 0,100% 100%,0 100%)}
</style>
</head>
<body>
<main class="sheet">
  <div class="top-stripe"></div>
  <div class="corner-band"></div>
  <div class="corner-band-red"></div>

  <header class="header">
    <svg class="alert-badge" viewBox="0 0 100 100" aria-hidden="true">
      <circle cx="50" cy="50" r="48" fill="#f7d7d7"/>
      <circle cx="50" cy="50" r="40" fill="#e02a2a"/>
      <rect x="45" y="24" width="10" height="36" rx="4" fill="#fff"/>
      <circle cx="50" cy="72" r="6" fill="#fff"/>
    </svg>
    <div>
      <h1 class="title"><span class="accent">PHISHING</span> AND SCAMS</h1>
      <p class="subtitle">How to detect, what to do<br>and how to avoid being scammed</p>
    </div>
  </header>

  <section>
    <div class="section-head">
      <svg class="section-icon" viewBox="0 0 100 100" aria-hidden="true">
        <circle cx="50" cy="50" r="48" fill="#1f4fb8"/>
        <rect x="24" y="28" width="52" height="34" rx="3" fill="none" stroke="#fff" stroke-width="5"/>
        <rect x="44" y="62" width="12" height="8" fill="#fff"/>
        <rect x="34" y="70" width="32" height="5" rx="2" fill="#fff"/>
        <circle cx="50" cy="45" r="7" fill="#e02a2a"/>
      </svg>
      <h2 class="section-title">DETECTION AND AWARENESS</h2>
      <div class="section-rule"></div>
    </div>

    <div class="checklist">
      <h3>Look at the senders email address</h3>
      <ul>
        <li><svg viewBox="0 0 30 30" aria-hidden="true"><circle cx="15" cy="15" r="14" fill="#2faa4a"/><path d="M8 15.5l4.5 4.5L22 10.5" fill="none" stroke="#fff" stroke-width="3" stroke-linecap="round" stroke-linejoin="round"/></svg>Senders From Email address is from your domain or a trusted domain</li>
        <li><svg viewBox="0 0 30 30" aria-hidden="true"><circle cx="15" cy="15" r="14" fill="#e02a2a"/><path d="M10 10l10 10M20 10L10 20" stroke="#fff" stroke-width="3" stroke-linecap="round"/></svg>Senders From Email address is from a random email address or freemail like mailbox or postnet account</li>
        <li><svg viewBox="0 0 30 30" aria-hidden="true"><circle cx="15" cy="15" r="14" fill="#e02a2a"/><path d="M10 10l10 10M20 10L10 20" stroke="#fff" stroke-width="3" stroke-linecap="round"/></svg>Senders From Email address is from the CEO / Accounts etc but the address is not your corporate domain for example casy@mailbox.example</li>
        <li><svg viewBox="0 0 30 30" aria-hidden="true"><circle cx="15" cy="15" r="14" fill="#e02a2a"/><path d="M10 10l10 10M20 10L10 20" stroke="#fff" stroke-width="3" stroke-linecap="round"/></svg>Sender is pretending to be an internal staff member but the email body has the "External Mail" pink bar warning.</li>
      </ul>

      <h3>Contain a link to reset password or scare tactic</h3>
      <ul>
        <li><svg viewBox="0 0 30 30" aria-hidden="true"><circle cx="15" cy="15" r="14" fill="#e02a2a"/><path d="M10 10l10 10M20 10L10 20" stroke="#fff" stroke-width="3" stroke-linecap="round"/></svg>Softmax, the bank, the Revenue Office and others will not ask you to click a link to reset your password</li>
        <li><svg viewBox="0 0 30 30" aria-hidden="true"><circle cx="15" cy="15" r="14" fill="#e02a2a"/><path d="M10 10l10 10M20 10L10 20" stroke="#fff" stroke-width="3" stroke-linecap="round"/></svg>Softmax, NetLink and others do not monitor your computer or network and advise you they detected an error click a link to resolve</li>
      </ul>
    </div>
  </section>

  <section class="bottom">
    <div class="hacked">
      <h2>DOES THIS MEAN <span class="accent">I WAS HACKED</span></h2>
      <div class="hacked-cards">
        <div class="info-card">
          <svg viewBox="0 0 80 80" aria-hidden="true"><circle cx="40" cy="40" r="38" fill="#e02a2a" stroke="#fff" stroke-width="4"/><rect x="35" y="18" width="10" height="30" rx="4" fill="#fff"/><circle cx="40" cy="59" r="6" fill="#fff"/></svg>
          There is a very strong likelihood you were not hacked, Scammers will obtain your email address from websites, Connectly or from numerous methods.
        </div>
        <div class="info-card">
          <svg viewBox="0 0 80 80" aria-hidden="true"><circle cx="40" cy="40" r="38" fill="#e02a2a" stroke="#fff" stroke-width="4"/><rect x="25" y="38" width="30" height="22" rx="3" fill="#fff"/><path d="M31 38v-7a9 9 0 0 1 18 0v7" fill="none" stroke="#fff" stroke-width="5"/></svg>
          Scammers are pretending to be someone else (phishing) or use a scare tactic to trick you into giving them your information / passwords or other fraud attempts.
        </div>
      </div>
    </div>

    <div class="todo">
      <h2>WHAT SHOULD<br>I DO?</h2>
      <p>You can safely ignore and delete the email and if in doubt, please contact Nexora Technology who can check and advise further.</p>
      <div class="brand"><span class="brand-mark"></span><span class="brand-name">NEXORA TECHNOLOGY</span></div>
      <p class="brand-tag">"ICT Solutions &amp; Engineering"</p>
      <ul class="contacts">
        <li><svg viewBox="0 0 34 34" aria-hidden="true"><circle cx="17" cy="17" r="16" fill="#e02a2a"/><path d="M11 9l4 1 1 4-2 2a10 10 0 0 0 5 5l2-2 4 1 1 4-2 1C16 25 9 18 9 11z" fill="#fff"/></svg>1300 000 482</li>
        <li><svg viewBox="0 0 34 34" aria-hidden="true"><circle cx="17" cy="17" r="16" fill="#e02a2a"/><rect x="8" y="11" width="18" height="13" rx="1.5" fill="#fff"/><path d="M8.5 12l8.5 7 8.5-7" fill="none" stroke="#e02a2a" stroke-width="1.8"/></svg>help@nexora-tech.example</li>
        <li><svg viewBox="0 0 34 34" aria-hidden="true"><circle cx="17" cy="17" r="16" fill="#e02a2a"/><circle cx="17" cy="17" r="9" fill="none" stroke="#fff" stroke-width="2"/><ellipse cx="17" cy="17" rx="4" ry="9" fill="none" stroke="#fff" stroke-width="2"/><path d="M8 17h18" stroke="#fff" stroke-width="2"/></svg>www.nexora-tech.example</li>
      </ul>
    </div>
  </section>

  <div class="footer-red"></div>
  <footer class="footer"></footer>
</main>
</body>
</html>
```